Business Card Design Project

for a second hand vintage clothing store. shop name is The Velvet Cupboard

Cards to be double sided

The name on the card is Joanna Whitfield

Information to put on card:

The Velvet Cupboard
Joanna Whitfield (no job title)
42/871 Dunmore St, Glenwick, Sydney, NSW, 2009.
Mobile: 0412 905 261
Email: thevelvetcupboard@mailbox.com.au
Web: www.thevelvetcupboard.com.au

Target Market(s)

Women looking at vintage clothing

Industry/Entity Type

Clothing

```html
<!DOCTYPE html>
<html lang="en">
<head>
<meta charset="utf-8">
<title>The Velvet Cupboard – Business Card</title>
<link href="https://fonts.googleapis.com/css2?family=Oswald:wght@500;700&family=Roboto+Condensed:wght@300;400&display=swap" rel="stylesheet">
<style>
  :root {
    --backdrop: #2c2c2e;
    --cream: #e4d59d;
    --plum: #4e2636;
    --plum-deep: #3e1d2b;
    --ink: #2f2428;
    --name-plum: #5b2a4a;
    --shop-plum: #3d1f35;
    --rule: #4a3a3e;
  }
  * { box-sizing: border-box; margin: 0; padding: 0; }
  html, body { width: 1200px; height: 800px; overflow: hidden; }
  body {
    background: var(--backdrop);
    position: relative;
    font-family: "Roboto Condensed", "Arial Narrow", sans-serif;
  }
  .card {
    position: absolute;
    top: 130px;
    width: 330px;
    height: 540px;
    overflow: hidden;
    box-shadow: 0 10px 30px rgba(0,0,0,.45);
  }
  .card--front { left: 210px; background: var(--cream); }
  .card--back  { left: 660px; background: var(--plum); }

  /* Content is laid out landscape, then turned to read along the card */
  .face {
    position: absolute;
    left: -105px;
    top: 105px;
    width: 540px;
    height: 330px;
    transform: rotate(90deg);
  }
  .edge-bands { position: absolute; inset: 0; width: 540px; height: 330px; }
  .card--front .edge-bands path { fill: var(--plum); }
  .card--back .edge-bands path { fill: var(--cream); }

  .watermark {
    position: absolute;
    left: 40px;
    top: 110px;
    font-family: "Roboto Condensed", "Arial Narrow", sans-serif;
    font-weight: 300;
    font-size: 78px;
    letter-spacing: 2px;
    white-space: nowrap;
  }
  .card--front .watermark { color: rgba(78,38,54,.10); }
  .card--back .watermark { color: rgba(228,213,157,.08); left: 30px; top: 150px; }

  .identity {
    position: absolute;
    right: 352px;
    top: 96px;
    text-align: right;
  }
  .identity__name {
    font-family: "Oswald", "Arial Narrow", sans-serif;
    font-weight: 700;
    font-size: 23px;
    line-height: 1;
    color: var(--name-plum);
  }
  .identity__shop {
    font-family: "Oswald", "Arial Narrow", sans-serif;
    font-weight: 500;
    font-size: 13px;
    margin-top: 4px;
    color: var(--shop-plum);
  }
  .divider {
    position: absolute;
    left: 198px;
    top: 96px;
    width: 1px;
    height: 62px;
    background: var(--rule);
  }
  .contact {
    position: absolute;
    left: 208px;
    top: 94px;
    list-style: none;
    font-weight: 400;
    font-size: 11.5px;
    line-height: 15.5px;
    color: var(--ink);
  }
  .shop-name {
    position: absolute;
    font-family: "Roboto Condensed", "Arial Narrow", sans-serif;
    font-weight: 400;
    white-space: nowrap;
  }
  .card--front .shop-name {
    left: 110px;
    top: 210px;
    font-size: 30px;
    color: var(--ink);
  }
  .card--back .shop-name {
    left: 0;
    right: 0;
    top: 140px;
    text-align: center;
    font-size: 40px;
    color: var(--cream);
  }
</style>
</head>
<body>

<section class="card card--front" aria-label="Card front">
  <div class="face">
    <svg class="edge-bands" viewBox="0 0 540 330" aria-hidden="true">
      <path d="M22,0 Q42,30 92,30 H448 Q498,30 518,0 Z"/>
      <path d="M22,330 Q42,300 92,300 H448 Q498,300 518,330 Z"/>
    </svg>
    <div class="watermark" aria-hidden="true">The Velvet Cupboard</div>
    <div class="identity">
      <p class="identity__name">Joanna Whitfield</p>
      <p class="identity__shop">The Velvet Cupboard</p>
    </div>
    <div class="divider"></div>
    <ul class="contact">
      <li>Tel: 0412 905 261</li>
      <li>Web: www.thevelvetcupboard.com.au</li>
      <li>Email: thevelvetcupboard@mailbox.com.au</li>
      <li>42/871 Dunmore St, Glenwick, Sydney, NSW, 2009</li>
    </ul>
    <p class="shop-name">The Velvet Cupboard</p>
  </div>
</section>

<section class="card card--back" aria-label="Card back">
  <div class="face">
    <svg class="edge-bands" viewBox="0 0 540 330" aria-hidden="true">
      <path d="M22,0 Q42,30 92,30 H448 Q498,30 518,0 Z"/>
      <path d="M22,330 Q42,300 92,300 H448 Q498,300 518,330 Z"/>
    </svg>
    <div class="watermark" aria-hidden="true">The Velvet Cupboard</div>
    <p class="shop-name">The Velvet Cupboard</p>
  </div>
</section>

</body>
</html>
```